Business Card: RW Office Partners - Your organised problem solver

Business Name: RW Office Partners
Website: www.rwofficepartners-example.com.au
Email: maribel@rwofficepartners-example.com.au
Mobile: 61 400 000 000
Facebook: @rwofficepartners
Instrgram: @rwofficepartners

Brading Colours:
HEX
#986474
#ddccd3
#7a8498
#c9d8e4
#000000
#ffffff

Tag Line: Your dependable office ally

Link to DRAFT website:
https://draftsites-example.com/rw-office-partners

About Page from the website:
My name is Maribel Rowe, and I would love to assist you to become more productive in your day to day and achieve your business and personal goals.
My mission is to give you time, time to work on the important tasks of your business or to be able to spend more time with your family. I will take on the tasks you don’t have time for, don’t know well or simply don’t like to do.
I have an extensive background in Administration, Tender Coordination, Document Control, WHS and Quality Management working primarily in the Construction, Mining and Corporate World.
I am passionate about being organised, having order and making things in your life (and mine) easier! I love to watch something unfold and grow into something amazing! I am known for being the go-to problem solver, the organiser of all things, producing high standards of work even under pressure. I’m also a confident communicator, and I understand that you’re busy running your business.

Target Market(s)

Small to Medium Business who require assistance in their business by a virtual assistant.

Industry/Entity Type

Virtual Assistant

Contact Information for Business Card

Mobile: 61 400 000 000

Font styles to use
Sans Serif

Colors
ffffff

Requirements
Must have
• Branding Colours as outlined.
Contact Details as outlined.
Logo as provided.
Proper contact details - mobile, facebook, instragm, website.
Simple, Elegant, very clean looking.
Should not have
• Note cute with pictures.
Not too girly as still want to market to construction companies.

```html
<!DOCTYPE html>
<html lang="en">
<head>
<meta charset="utf-8">
<title>RW Office Partners - Business Card</title>
<link rel="stylesheet" href="https://fonts.googleapis.com/css2?family=Montserrat:wght@600&family=Open+Sans:wght@400&family=Roboto:wght@300&display=swap">
<style>
  :root {
    --page-bg: #e9e6e4;
    --card-bg: #f1f0ef;
    --slate: #5f687b;
    --slate-dark: #4a5266;
    --maroon: #85606c;
    --maroon-deep: #5a3442;
    --line-light: #ddccd3;
    --white: #ffffff;
  }
  html, body {
    margin: 0;
    padding: 0;
    width: 1200px;
    height: 970px;
    overflow: hidden;
    background: var(--page-bg);
  }
  .card {
    position: absolute;
    left: 174px;
    top: 272px;
    width: 852px;
    height: 472px;
    border-radius: 26px;
    overflow: hidden;
    background: var(--card-bg);
    box-shadow: 0 8px 24px rgba(0,0,0,0.14);
  }
  .brand-name {
    position: absolute;
    left: 0;
    right: 0;
    top: 92px;
    text-align: center;
    font-family: "Montserrat", sans-serif;
    font-weight: 600;
    font-size: 44px;
    line-height: 46px;
    letter-spacing: 1px;
    color: var(--slate-dark);
    text-transform: uppercase;
  }
  .tagline-band {
    position: absolute;
    left: 0;
    right: 0;
    top: 252px;
    height: 50px;
    background: var(--slate);
    color: var(--white);
    font-family: "Open Sans", sans-serif;
    font-size: 26px;
    line-height: 50px;
    text-align: center;
  }
  .contact-band {
    position: absolute;
    left: 0;
    right: 0;
    top: 304px;
    bottom: 0;
    background: linear-gradient(90deg, var(--maroon) 0%, #7d5563 45%, var(--maroon-deep) 100%);
    border-top: 2px solid var(--line-light);
  }
  .contact-text {
    position: absolute;
    font-family: "Roboto", sans-serif;
    font-weight: 300;
    font-size: 20px;
    line-height: 26px;
    color: var(--line-light);
    white-space: nowrap;
  }
  .contact-left { right: 522px; text-align: right; }
  .contact-right { left: 436px; }
  .icon {
    position: absolute;
    width: 20px;
    height: 20px;
  }
  .divider {
    position: absolute;
    left: 379px;
    top: 28px;
    width: 2px;
    height: 102px;
    background: var(--line-light);
  }
</style>
</head>
<body>
  <div class="card">
    <div class="brand-name">RW Office<br>Partners</div>

    <div class="tagline-band">Your dependable office ally</div>

    <div class="contact-band">
      <div class="contact-text contact-left" style="top:53px;">61 400 000 000</div>
      <svg class="icon" style="left:342px; top:56px;" viewBox="0 0 20 20" aria-label="Mobile">
        <rect x="5" y="1" width="10" height="18" rx="2" fill="none" stroke="#ddccd3" stroke-width="1.6"/>
        <line x1="8" y1="16" x2="12" y2="16" stroke="#ddccd3" stroke-width="1.6"/>
      </svg>

      <div class="contact-text contact-left" style="top:85px;">@rwofficepartners</div>
      <svg class="icon" style="left:342px; top:88px;" viewBox="0 0 20 20" aria-label="Social profile">
        <rect x="5" y="4" width="11" height="12" fill="#ddccd3"/>
      </svg>

      <div class="divider"></div>

      <svg class="icon" style="left:400px; top:38px;" viewBox="0 0 20 20" aria-label="Email">
        <rect x="1" y="4" width="18" height="12" fill="none" stroke="#ddccd3" stroke-width="1.5"/>
        <polyline points="1,4 10,11 19,4" fill="none" stroke="#ddccd3" stroke-width="1.5"/>
      </svg>
      <div class="contact-text contact-right" style="top:35px;">maribel@rwofficepartners-example.com.au</div>

      <svg class="icon" style="left:400px; top:65px;" viewBox="0 0 20 20" aria-label="Website">
        <circle cx="10" cy="10" r="8" fill="none" stroke="#ddccd3" stroke-width="1.5"/>
        <ellipse cx="10" cy="10" rx="3.5" ry="8" fill="none" stroke="#ddccd3" stroke-width="1.2"/>
        <line x1="2" y1="10" x2="18" y2="10" stroke="#ddccd3" stroke-width="1.2"/>
        <line x1="3.5" y1="6" x2="16.5" y2="6" stroke="#ddccd3" stroke-width="1"/>
        <line x1="3.5" y1="14" x2="16.5" y2="14" stroke="#ddccd3" stroke-width="1"/>
      </svg>
      <div class="contact-text contact-right" style="top:62px;">www.rwofficepartners-example.com.au</div>

      <svg class="icon" style="left:400px; top:93px;" viewBox="0 0 20 20" aria-label="Photo profile">
        <rect x="2" y="2" width="16" height="16" fill="none" stroke="#ddccd3" stroke-width="1.5"/>
      </svg>
      <div class="contact-text contact-right" style="top:90px;">@rwofficepartners</div>
    </div>
  </div>
</body>
</html>
```